Cricket Protein Balls- Packaging design

We are re-designing our current artwork for our protein balls made from cricket flour. Cricket flour is a sustainable and environmentally friendly source of protein. There are 2 varieties (so we will require 2 label designs)

Required on the label will be-

Our logo (see attached)
Name of product
A small section to one side to contain text (on one edge)- Exact text will be updated shortly. So please enter filler text until actual is supplied.

The first products name will be- Cacao, Cranberry & Chia Orvin Pops

The second variety is- Chilli & Lime Orvin Pops

Please do not include photographs of bugs on the label design. Silhouettes or drawings are OK.

The design will be for a label (sticker) which will be applied to the front of a curved deli cup container. The label design should be curved slightly to allow for bend in container. Approx dimensions will be 3cm (h) x 10cm (l)

Colours below are given as a guide only- please feel free to be creative if you have another colour pallet in mind

Target Market(s)

This product is aimed at consumers who are interested in the paleo diet, environmental issues and body builders (high protein).

Industry/Entity Type

Product

Colors
acd037
cadf82
faee3f
34b8a4
86cfc6
b7a5cd
8768ae

Requirements
Must have
• bright eye catching design with environmental/sustainable feel.

Text must be easy to read

```html
<!DOCTYPE html>
<html lang="en">
<head>
<meta charset="utf-8">
<title>Cacao Orvin Pops – Label Set</title>
<link rel="stylesheet" href="https://fonts.googleapis.com/css2?family=Chewy&family=Patrick+Hand&family=Open+Sans:wght@400&display=swap">
<style>
  :root {
    --page: #ffffff;
    --purple: #8f70c2;
    --red: #e8372f;
    --gap-white: #ffffff;
    --cacao-yellow: #f7e93c;
    --subtitle-white: #ffffff;
    --info-green: #9cc43a;
    --info-text: #ffffff;
    --brand-green: #7f9a2a;
    --brand-light: #cadf82;
    --divider: #9a9a9a;
  }
  * { box-sizing: border-box; margin: 0; padding: 0; }
  html, body {
    width: 1200px;
    height: 792px;
    overflow: hidden;
    background: var(--page);
  }
  .sheet {
    position: relative;
    width: 1200px;
    height: 792px;
  }
  .label {
    position: absolute;
    left: 0;
    width: 1200px;
    height: 360px;
  }
  .label--cranberry { top: 21px; --label-colour: var(--purple); }
  .label--chilli { top: 411px; --label-colour: var(--red); }

  .label__panels {
    position: absolute;
    inset: 0;
    width: 1200px;
    height: 360px;
  }
  .label__panels .panel { fill: var(--label-colour); }
  .label__panels .panel--brand { filter: drop-shadow(6px 6px 6px rgba(0,0,0,0.25)); }

  .brand {
    position: absolute;
    left: 62px;
    top: 118px;
    display: flex;
    align-items: center;
    gap: 12px;
  }
  .brand__dot {
    width: 34px;
    height: 34px;
    border-radius: 50%;
    background: var(--brand-light);
    flex: none;
  }
  .brand__name {
    font-family: "Chewy", cursive;
    font-size: 44px;
    line-height: 46px;
    color: var(--brand-light);
    width: 220px;
  }

  .product {
    position: absolute;
    left: 507px;
    top: 62px;
  }
  .product__name {
    font-family: "Chewy", cursive;
    font-size: 104px;
    line-height: 100px;
    color: var(--cacao-yellow);
    text-shadow: 3px 4px 6px rgba(0,0,0,0.25);
    letter-spacing: 2px;
  }
  .product__variety {
    margin-left: 60px;
    margin-top: 6px;
    font-family: "Patrick Hand", cursive;
    font-size: 46px;
    line-height: 50px;
    color: var(--subtitle-white);
    letter-spacing: 1px;
    text-shadow: 2px 3px 5px rgba(0,0,0,0.3);
  }

  .info-box {
    position: absolute;
    left: 523px;
    top: 250px;
    width: 613px;
    height: 73px;
    padding: 10px 18px;
    background: var(--info-green);
    box-shadow: 5px 6px 8px rgba(0,0,0,0.3);
    font-family: "Open Sans", sans-serif;
    font-size: 15.5px;
    line-height: 25px;
    color: var(--info-text);
  }

  .cut-line {
    position: absolute;
    left: 0;
    top: 396px;
    width: 1200px;
    border-top: 2px dashed var(--divider);
  }
</style>
</head>
<body>
<main class="sheet">

  <section class="label label--cranberry">
    <svg class="label__panels" viewBox="0 0 1200 360" aria-hidden="true">
      <polygon class="panel panel--main" points="373,0 1200,0 1200,360 373,360 547,180"/>
      <polygon class="panel panel--brand" points="253,0 367,0 460,180 367,360 253,360 40,180"/>
    </svg>
    <div class="brand">
      <span class="brand__dot"></span>
      <span class="brand__name">Cricket Pantry</span>
    </div>
    <div class="product">
      <h1 class="product__name">Cacao</h1>
      <p class="product__variety">Cranberry &amp; Chia orvin pops</p>
    </div>
    <p class="info-box">Lorem ipsum dolor sit amet, consectetur adipisicing elit, sed do eiusmod tempor incididunt ut labore et dolore magna aliqua.</p>
  </section>

  <div class="cut-line"></div>

  <section class="label label--chilli">
    <svg class="label__panels" viewBox="0 0 1200 360" aria-hidden="true">
      <polygon class="panel panel--main" points="373,0 1200,0 1200,360 373,360 547,180"/>
      <polygon class="panel panel--brand" points="253,0 367,0 460,180 367,360 253,360 40,180"/>
    </svg>
    <div class="brand">
      <span class="brand__dot"></span>
      <span class="brand__name">Cricket Pantry</span>
    </div>
    <div class="product">
      <h1 class="product__name">Cacao</h1>
      <p class="product__variety">Chilli &amp; lime orvin pops</p>
    </div>
    <p class="info-box">Lorem ipsum dolor sit amet, consectetur adipisicing elit, sed do eiusmod tempor incididunt ut labore et dolore magna aliqua.</p>
  </section>

</main>
</body>
</html>
```